Summit In Boots Flyer, eyecatching

Hi,
To give you an idea of the business for design purposes, #SummitttInBoots is predominantly a recruitment and people development business, ran by me dedicated to training & assisting others in achieving extra income (pt or f/t) around their current commitments, people also have the opportunity to build their own business brand with my support. My brand colours are Red, White and Black, and I would like to incorporate the following text;

#SummitInBoots

Recruiting now! Start today & start earning!

Would you like an extra income, for…
A holiday?…A new car?…Lifestyle changes?
(Can you put a tick box or something similar adjacent to each)

Are you facing…
Redundancy? Birth of a new child? Hefty bills?

If so, I have the solution.

Contact Rosalind Pawley today: (can you insert the appropriate icon for each of the contact details)
Tel: 07941 608274
Twitter: @Summit_InBoots
Email: Rosalind@summitinboots-example.co.uk
Facebook: www.linkloop-example.com/rosandbrightstep

Target Market(s)

Women aged 25-45 years, possibly busy mums too, wanting to earn additinal income to allow them more choices, be it family time, money, new challenge, meeting new people, personal development

Industry/Entity Type

Health And Wellness

Font styles to use
Serif
Sans Serif
Decorative
Script

Colors
ec1f27
ffffff
000000

Requirements
Must have
• My heels logo, be clear concise and eye catching, I also have the following strap line if you wish to use;
• Empowering other to achieve
• Also I have attached a closeup picture of myself but would ideally only like half my face to appear (leftside) similar to the other picture posted - if you can
Nice to have
• Perhaps adding other forms of graphics, or the 3rd picture I have attached with myself...possibly just the shoes though
Should not have
• Too many colours

```html
<!DOCTYPE html>
<html lang="en">
<head>
<meta charset="utf-8">
<title>Brightstep – Recruiting Flyer</title>
<link href="https://fonts.googleapis.com/css2?family=Oswald:wght@300;400&family=Roboto+Condensed:wght@300;400&display=swap" rel="stylesheet">
<style>
  :root {
    --red: #b51c24;
    --red-icon: #c0222a;
    --white: #ffffff;
    --charcoal: #2a2a2a;
    --ink: #1e1e1e;
    --cream: #fbfbe9;
    --straw: #e4e394;
    --lime-rule: #d9dc8a;
    --blush-rule: #e59a93;
    --badge-blue: #3b8fd9;
  }
  * { margin: 0; padding: 0; box-sizing: border-box; }
  html, body { width: 850px; height: 1200px; overflow: hidden; background: var(--white); }
  .flyer { position: relative; width: 850px; height: 1200px; overflow: hidden; font-family: "Roboto Condensed", sans-serif; color: var(--ink); }

  /* header */
  .hero { position: absolute; left: 0; top: 0; width: 850px; height: 300px; overflow: hidden; background: var(--white); }
  .hero-photo-left { position: absolute; left: 0; top: 0; width: 406px; height: 300px;
    background: linear-gradient(90deg, #d9d4cf 0%, #6e5f56 30%, #4a3d36 45%, #e9e7e4 70%, #f4f3f1 100%); }
  .hero-photo-right { position: absolute; left: 436px; top: 0; width: 414px; height: 300px;
    background: linear-gradient(160deg, #f1f0ee 0%, #e6c3b4 35%, #d9a896 65%, #c48f7e 100%); }
  .hero-dome { position: absolute; left: 126px; top: 52px; width: 590px; height: 590px; border-radius: 50%; background: var(--white); }
  .brand-name { position: absolute; left: 0; width: 850px; top: 236px; text-align: center;
    font-family: "Roboto Condensed", sans-serif; font-weight: 400; font-size: 46px; letter-spacing: 0; color: var(--ink); }

  .rule-lime { position: absolute; left: 0; top: 300px; width: 850px; height: 3px; background: var(--lime-rule); }
  .banner { position: absolute; left: 0; top: 303px; width: 850px; height: 65px; background: var(--charcoal);
    color: var(--white); font-family: "Roboto Condensed", sans-serif; font-size: 40px; line-height: 65px; text-align: center; font-weight: 400; }

  /* questions */
  .questions { position: absolute; left: 0; top: 368px; width: 850px; height: 416px;
    background: radial-gradient(ellipse at 50% 50%, var(--white) 0%, var(--cream) 40%, var(--straw) 100%); }
  .question { position: absolute; left: 0; width: 850px; text-align: center; font-family: "Roboto Condensed", sans-serif; font-size: 34px; font-weight: 400; color: var(--ink); }
  .q-income { top: 12px; }
  .q-facing { top: 226px; }
  .option { position: absolute; width: 200px; text-align: center; }
  .option svg { display: block; margin: 0 auto; }
  .option-label { display: block; margin-top: 6px; font-size: 22px; font-family: "Oswald", sans-serif; font-weight: 400; color: var(--ink); }

  /* contact */
  .contact { position: absolute; left: 0; top: 784px; width: 850px; height: 344px; background: var(--red); border-top: 3px solid var(--blush-rule); }
  .portrait-frame { position: absolute; left: 26px; top: 30px; width: 256px; height: 292px; background: var(--white); padding: 9px; }
  .portrait { width: 100%; height: 100%;
    background: linear-gradient(170deg, #f2efed 0%, #e8cfc6 35%, #d8aa9b 60%, #a04650 85%, #2b2b2b 100%); }
  .pitch { position: absolute; left: 306px; top: 44px; color: var(--white); font-family: "Oswald", sans-serif; font-weight: 400; font-size: 40px; line-height: 58px; }
  .contact-list { position: absolute; left: 306px; top: 186px; list-style: none; }
  .contact-list li { display: flex; align-items: center; height: 33px; color: var(--white); font-family: "Oswald", sans-serif; font-weight: 400; font-size: 22px; }
  .contact-list svg { width: 28px; height: 28px; margin-right: 25px; flex: none; }
  .dot-badge { fill: var(--badge-blue); }

  .rule-blush { position: absolute; left: 0; top: 1128px; width: 850px; height: 3px; background: var(--blush-rule); }
  .footer { position: absolute; left: 0; top: 1131px; width: 850px; height: 69px; background: var(--charcoal);
    color: var(--white); text-align: center; line-height: 66px; font-size: 17px; letter-spacing: 0.45em; }
</style>
</head>
<body>
<main class="flyer">

  <header class="hero">
    <div class="hero-photo-left" role="img" aria-label="Photo of a woman with platinum hair in profile"></div>
    <div class="hero-photo-right" role="img" aria-label="Close-up photo of a made-up blue eye"></div>
    <div class="hero-dome"></div>
    <div class="brand-name">Brightstep</div>
  </header>

  <div class="rule-lime"></div>
  <div class="banner">Recruiting now! Start today &amp; start earning!</div>

  <section class="questions">
    <h2 class="question q-income">Wouldyoulike an extra income, for…</h2>

    <div class="option" style="left:110px; top:74px">
      <svg width="82" height="82" viewBox="0 0 82 82"><circle cx="41" cy="41" r="40" fill="var(--red-icon)" stroke="#f3d3d0" stroke-width="2"/>
        <path d="M18 60 Q41 50 64 60 Z" fill="#fff"/><path d="M14 66 H68" stroke="#fff" stroke-width="3"/>
        <path d="M41 56 Q40 38 44 26" stroke="#fff" stroke-width="4" fill="none"/>
        <path d="M44 26 Q32 18 24 28 Q34 24 44 26 Q40 14 30 14 Q40 18 44 26 Q50 14 60 18 Q50 20 44 26 Q58 24 60 34 Q52 26 44 26Z" fill="#fff"/></svg>
      <span class="option-label">A holiday?</span>
    </div>
    <div class="option" style="left:320px; top:74px">
      <svg width="82" height="82" viewBox="0 0 82 82"><circle cx="41" cy="41" r="40" fill="var(--red-icon)" stroke="#f3d3d0" stroke-width="2"/>
        <path d="M16 40 L24 24 H58 L66 40 V56 H60 V62 H52 V56 H30 V62 H22 V56 H16 Z" fill="#fff"/>
        <path d="M27 28 H55 L60 39 H22 Z" fill="var(--red-icon)"/>
        <circle cx="25" cy="47" r="4" fill="var(--red-icon)"/><circle cx="57" cy="47" r="4" fill="var(--red-icon)"/></svg>
      <span class="option-label">A new car?</span>
    </div>
    <div class="option" style="left:530px; top:74px">
      <svg width="82" height="82" viewBox="0 0 82 82"><circle cx="41" cy="41" r="40" fill="var(--red-icon)" stroke="#f3d3d0" stroke-width="2"/>
        <rect x="18" y="38" width="11" height="24" rx="2" fill="#fff"/>
        <path d="M32 38 L42 20 Q47 18 47 24 L45 34 H60 Q65 35 63 41 L58 58 Q56 62 51 62 H32 Z" fill="#fff"/></svg>
      <span class="option-label">Lifestyle changes?</span>
    </div>

    <h2 class="question q-facing">Are you facing…</h2>

    <div class="option" style="left:110px; top:282px">
      <svg width="82" height="82" viewBox="0 0 82 82"><circle cx="41" cy="41" r="40" fill="var(--red-icon)" stroke="#f3d3d0" stroke-width="2"/>
        <path d="M22 38 A19 19 0 0 1 56 28" stroke="#fff" stroke-width="6" fill="none"/>
        <path d="M52 18 L62 30 L48 32 Z" fill="#fff"/>
        <path d="M60 44 A19 19 0 0 1 26 54" stroke="#fff" stroke-width="6" fill="none"/>
        <path d="M30 64 L20 52 L34 50 Z" fill="#fff"/></svg>
      <span class="option-label">Redundancy?</span>
    </div>
    <div class="option" style="left:320px; top:282px">
      <svg width="82" height="82" viewBox="0 0 82 82"><circle cx="41" cy="41" r="40" fill="var(--red-icon)" stroke="#f3d3d0" stroke-width="2"/>
        <circle cx="41" cy="20" r="7" fill="#fff"/>
        <path d="M24 34 Q41 26 58 34 L56 38 L48 36 V48 H34 V36 L26 38 Z" fill="#fff"/>
        <path d="M34 50 H48 L52 58 L44 66 L41 60 L38 66 L30 58 Z" fill="#fff"/></svg>
      <span class="option-label">Birth of a new child?</span>
    </div>
    <div class="option" style="left:530px; top:282px">
      <svg width="82" height="82" viewBox="0 0 82 82"><circle cx="41" cy="41" r="40" fill="var(--red-icon)" stroke="#f3d3d0" stroke-width="2"/>
        <rect x="24" y="16" width="32" height="46" transform="rotate(8 40 39)" fill="#fff"/>
        <g transform="rotate(8 40 39)" stroke="var(--red-icon)" stroke-width="1.5">
          <path d="M28 22 H48"/><path d="M28 30 H52"/><path d="M28 36 H52"/><path d="M28 42 H52"/><path d="M28 48 H52"/><path d="M28 54 H46"/></g></svg>
      <span class="option-label">Hefty bills?</span>
    </div>
  </section>

  <section class="contact">
    <div class="portrait-frame"><div class="portrait" role="img" aria-label="Portrait photo of Rosalind Pawley with red nails"></div></div>
    <p class="pitch">If so, I have the solution.<br>Contact Rosalind Pawley today</p>
    <ul class="contact-list">
      <li><svg viewBox="0 0 26 26"><path d="M2 9 Q13 2 24 9 L22 12 L18 10 V8 H8 V10 L4 12 Z" fill="#fff"/><path d="M7 12 H19 L22 22 H4 Z" fill="#fff"/><circle cx="13" cy="17" r="3" fill="var(--red)"/></svg>07941 608274</li>
      <li><svg viewBox="0 0 26 26"><circle class="dot-badge" cx="13" cy="13" r="12"/></svg>@Summit_InBoots</li>
      <li><svg viewBox="0 0 26 26"><circle cx="13" cy="13" r="4.5" stroke="#fff" stroke-width="2.5" fill="none"/><path d="M17.5 9 V15 Q17.5 18 20.5 18 Q24 18 24 13 A11 11 0 1 0 18 23" stroke="#fff" stroke-width="2.5" fill="none"/></svg>Rosalind@summitinboots-example.co.uk</li>
      <li><svg viewBox="0 0 26 26"><circle class="dot-badge" cx="13" cy="13" r="12"/></svg>www.linkloop-example.com/rosandbrightstep</li>
    </ul>
  </section>

  <div class="rule-blush"></div>
  <footer class="footer">WWW.BRIGHTSTEP-EXAMPLE.COM</footer>

</main>
</body>
</html>
```